Create Product Deck for Organic Beard Oil Brand

We need a product deck to showcase our beard oil collection to potential buyers from department stores, barbershops/salons and wholesale buyers. Attached is a perfect example of the style and layout we want for our product deck.The info regarding the brand should include the following:Company BioPerformance Month OverviewGlobal Reach ShowcaseThe info for each product should include the following:Product NameSKU and/or UPCProduct DescriptionCase SizeWholesale PricingRetail PricingIngredients

Target Market(s)

Men with beards in the U.S.

Women who are married or in a relationship with a bearded man.

Ethnicity: African-American/Multicutural/White

Ages: 24 - 45

Middle Class / Fathers / Married / Dating / Single

Industry/Entity Type

Hair And Beauty

Font styles to use
Sans Serif
Other font styles liked:
• ITC Franklin Gothic

Colors
acd036
0692cd
f04a50

Requirements
Must have
• Must be bright, colorful and showcase each of the products highlighting their particular scents.
• List of our products to be shown in product deck:
• Mango Basil Beard Oil
• Warm Hazel Beard Oil
• Bold As Brass Beard Oil
• Teal Otter Beard Oil
• Evening Tide Beard Oil
• House Reserve Beard Oil
• Images for each of these products have been included as well.
Nice to have
• Surprise me by showing off your personal flash and flare. Do not let our color preferences restrict you from this.
Should not have
• No "bro culture" copy.
• No woodsmen/lumberjack styles like other beard brands have.

```html
<!DOCTYPE html>
<html lang="en">
<head>
<meta charset="utf-8">
<title>Digital Marketing Takeover – January Performance Overview</title>
<link rel="stylesheet" href="https://fonts.googleapis.com/css2?family=Libre+Franklin:wght@500;800;900&display=swap">
<style>
  :root {
    --lime: #acd036;
    --lime-light: #bfdc45;
    --lime-deep: #8dba1f;
    --white: #ffffff;
    --screen-dark: #3a3d40;
    --screen-mid: #8a8f93;
    --base-light: #d9dbdd;
    --base-dark: #9a9ea2;
  }
  * { margin: 0; padding: 0; box-sizing: border-box; }
  html, body { width: 1200px; height: 927px; overflow: hidden; }
  body {
    font-family: "Libre Franklin", "Franklin Gothic Medium", Arial, sans-serif;
    color: var(--white);
  }
  .slide {
    position: relative;
    width: 1200px;
    height: 927px;
    background: radial-gradient(ellipse at 50% 35%, var(--lime-light) 0%, var(--lime) 45%, var(--lime-deep) 100%);
    overflow: hidden;
  }
  .headline {
    position: absolute;
    left: 74px;
    top: 102px;
    text-transform: uppercase;
  }
  .headline__title {
    font-weight: 900;
    font-size: 47px;
    line-height: 1;
    letter-spacing: 0.2px;
  }
  .headline__subtitle {
    font-weight: 800;
    font-size: 27px;
    line-height: 1;
    margin-top: 9px;
    letter-spacing: 0.3px;
  }
  .showcase {
    position: absolute;
    left: 293px;
    top: 280px;
    width: 614px;
    height: 404px;
    border-radius: 14px 14px 0 0;
    background: linear-gradient(180deg, var(--screen-dark) 0%, var(--screen-mid) 100%);
  }
  .showcase-base {
    position: absolute;
    left: 190px;
    top: 684px;
    width: 819px;
    height: 30px;
    border-radius: 0 0 40px 40px;
    background: linear-gradient(180deg, var(--base-light) 0%, var(--base-dark) 100%);
  }
  .stat {
    position: absolute;
    width: 220px;
    text-align: center;
  }
  .stat__icon { display: block; margin: 0 auto; fill: var(--white); }
  .stat__value {
    font-weight: 900;
    font-size: 68px;
    line-height: 1;
    letter-spacing: -1px;
  }
  .stat__label {
    font-weight: 500;
    font-size: 23px;
    line-height: 1.1;
    margin-top: 2px;
  }
  .stat--orders { left: 34px; top: 289px; }
  .stat--impressions { left: 34px; top: 522px; }
  .stat--reach { left: 934px; top: 300px; }
  .stat--emails { left: 934px; top: 518px; }
  .stat--orders .stat__icon { margin-bottom: 4px; }
  .stat--impressions .stat__icon { margin-bottom: 8px; }
  .stat--reach .stat__icon { margin-bottom: 4px; }
  .stat--emails .stat__icon { margin-bottom: 8px; }

  .visitors {
    position: absolute;
    left: 0;
    top: 772px;
    width: 1200px;
    text-align: center;
  }
  .visitors__row {
    display: inline-flex;
    align-items: center;
    gap: 10px;
  }
  .visitors__value {
    font-weight: 900;
    font-size: 69px;
    line-height: 1;
    letter-spacing: -1px;
  }
  .visitors__label {
    font-weight: 500;
    font-size: 24px;
    margin-top: 8px;
  }
</style>
</head>
<body>
<main class="slide">
  <header class="headline">
    <h1 class="headline__title">Digital Marketing Takeover</h1>
    <p class="headline__subtitle">Month of January Performance Overview</p>
  </header>

  <div class="showcase" role="img" aria-label="Laptop screen displaying the online store page with the beard oil customer favourites"></div>
  <div class="showcase-base" aria-hidden="true"></div>

  <section class="stat stat--orders">
    <svg class="stat__icon" width="48" height="50" viewBox="0 0 52 50" aria-hidden="true">
      <path d="M14 18 L26 4 L38 18" fill="none" stroke="#fff" stroke-width="4"/>
      <rect x="2" y="17" width="48" height="7" rx="2"/>
      <path d="M6 26 H46 L42 48 H10 Z"/>
      <rect x="14" y="29" width="4" height="15" fill="#acd036"/>
      <rect x="24" y="29" width="4" height="15" fill="#acd036"/>
      <rect x="34" y="29" width="4" height="15" fill="#acd036"/>
    </svg>
    <div class="stat__value">10K</div>
    <div class="stat__label">Website Orders</div>
  </section>

  <section class="stat stat--impressions">
    <svg class="stat__icon" width="84" height="34" viewBox="0 0 84 34" aria-hidden="true">
      <path d="M2 17 Q42 -12 82 17 Q42 46 2 17 Z"/>
      <circle cx="42" cy="17" r="12" fill="#acd036"/>
      <circle cx="42" cy="17" r="7"/>
    </svg>
    <div class="stat__value">20K</div>
    <div class="stat__label">Impressions</div>
  </section>

  <section class="stat stat--reach">
    <svg class="stat__icon" width="68" height="38" viewBox="0 0 68 38" aria-hidden="true">
      <circle cx="14" cy="10" r="7"/>
      <circle cx="54" cy="10" r="7"/>
      <circle cx="34" cy="8" r="8"/>
      <path d="M2 34 Q2 20 14 20 Q26 20 26 34 Z"/>
      <path d="M42 34 Q42 20 54 20 Q66 20 66 34 Z"/>
      <path d="M20 38 Q20 19 34 19 Q48 19 48 38 Z"/>
    </svg>
    <div class="stat__value">12K</div>
    <div class="stat__label">People Reached</div>
  </section>

  <section class="stat stat--emails">
    <svg class="stat__icon" width="58" height="36" viewBox="0 0 58 36" aria-hidden="true">
      <rect x="1" y="1" width="56" height="34" fill="none" stroke="#fff" stroke-width="3"/>
      <path d="M2 2 L29 22 L56 2" fill="none" stroke="#fff" stroke-width="3"/>
    </svg>
    <div class="stat__value">50K</div>
    <div class="stat__label">Emails Collected</div>
  </section>

  <section class="visitors">
    <div class="visitors__row">
      <svg width="70" height="56" viewBox="0 0 70 58" aria-hidden="true" fill="#fff">
        <rect x="2" y="2" width="66" height="44" rx="3" fill="none" stroke="#fff" stroke-width="4"/>
        <rect x="30" y="46" width="10" height="7"/>
        <rect x="20" y="52" width="30" height="5"/>
        <circle cx="24" cy="17" r="6"/>
        <circle cx="45" cy="17" r="6"/>
        <path d="M12 40 Q12 26 24 26 Q36 26 36 40 Z"/>
        <path d="M34 40 Q34 26 45 26 Q57 26 57 40 Z"/>
      </svg>
      <span class="visitors__value">500K</span>
    </div>
    <div class="visitors__label">Overall Website Visitors</div>
  </section>
</main>
</body>
</html>
```